Steadfast Claim Helpers USA - Email Marketing Creative

Looking for design of email creative for Steadfast Claim Helpers USA website. Call to action based email focused on conveying brand, messaging of "Disabled? Unable to Work? You May Qualify for Social Security Disability Benefits", call to action of 'Free Evaluation' or 'Fast, Free, No Obligation Evaluation'. Can use any messaging from the current mock of https://tinyvorn.com/7QpTz4M . Please focus on imaging of 50+ people if used, red white and blue coloring (patriotic) yet USA looking. Creative must be done in HTML as well as text for easy use and include Email Opt Out link etc. Examples of competitors emails attached. PLEASE DO NOT COPY them. Just use as examples.

Target Market(s)

Disabled American. Age 50+ Looking for help applying, re-applying or handling a social security disability hearing.

Industry/Entity Type

Legal

Font styles to use
Serif
Sans Serif

Colors

Requirements
Must have
• call to action based html
Nice to have
• strong call to action.
Should not have
• Should not be cookie cutter. Stick to simple yet official looking.

```html
<!DOCTYPE html>
<html lang="en">
<head>
<meta charset="utf-8">
<title>Steadfast Claim Helpers USA – Social Security Disability Benefits</title>
<link rel="stylesheet" href="https://fonts.googleapis.com/css2?family=Poppins:wght@400;500;600;700&display=swap">
<style>
:root{
  --navy:#1b2038;
  --navy-deep:#151a2e;
  --red:#e8232b;
  --white:#ffffff;
  --paper:#f2f2f2;
  --ink:#2b2b2b;
  --muted:#8a8a8a;
  --green:#22b02a;
}
*{box-sizing:border-box;margin:0;padding:0}
html,body{width:1200px;height:2668px;overflow:hidden}
body{font-family:"Poppins",sans-serif;background:var(--white);color:var(--ink);position:relative}

.site-header{position:absolute;left:0;top:0;width:1200px;height:144px;background:var(--white);display:flex;align-items:center;justify-content:space-between;padding:0 80px}
.brand{display:flex;align-items:center;gap:16px;font-weight:700;font-size:26px;color:var(--navy);line-height:1.1;text-transform:uppercase}
.brand-dot{width:52px;height:52px;border-radius:50%;background:var(--red);flex:none}
.main-nav{display:flex;gap:64px;font-size:22px;font-weight:500;color:var(--ink)}
.main-nav .active{color:var(--red)}

.hero{position:absolute;left:0;top:144px;width:1200px;height:688px;background:var(--navy);overflow:hidden}
.hero-photo{position:absolute;right:0;top:0;width:760px;height:688px;background:linear-gradient(135deg,#c9a58a 0%,#e6c9b2 40%,#9db46a 75%,#6c8f3c 100%)}
.hero-fade{position:absolute;left:0;top:0;width:1200px;height:688px;background:linear-gradient(90deg,var(--navy) 0%,var(--navy) 36%,rgba(27,32,56,.55) 55%,rgba(27,32,56,0) 72%)}
.hero-copy{position:absolute;left:80px;top:130px;color:var(--white)}
.hero-title{font-size:62px;font-weight:700;line-height:1.2}
.hero-sub{margin-top:28px;font-size:36px;font-weight:400;line-height:1.35}
.btn-primary{display:inline-block;margin-top:42px;background:var(--red);color:var(--white);font-size:30px;font-weight:600;padding:20px 40px;text-transform:uppercase}

.qualify{position:absolute;left:0;top:832px;width:1200px;height:1120px;background:var(--paper);padding:0 80px}
.qualify-title{margin-top:92px;text-align:center;font-size:44px;font-weight:600;color:#3a3a3a;line-height:1.3;text-transform:uppercase}
.qualify-title span{display:block;color:var(--red)}
.rule{width:160px;height:6px;background:var(--red);margin:22px auto 0}
.intro{margin-top:36px;font-size:30px;line-height:1.55;color:var(--muted)}
.checklist-title{margin-top:40px;font-size:36px;font-weight:600;color:var(--red)}
.checklist{list-style:none;margin-top:12px}
.checklist li{display:flex;align-items:center;gap:18px;font-size:28px;line-height:52px;color:#444}
.checklist svg{width:26px;height:26px;flex:none}

.services{position:absolute;left:80px;top:1604px;width:1040px;display:flex;justify-content:space-between}
.service{width:320px;text-align:center}
.service-icon{width:144px;height:144px;border-radius:50%;background:var(--navy);margin:0 auto;display:flex;align-items:center;justify-content:center}
.service-icon.is-green{background:var(--green)}
.service-icon svg{width:70px;height:70px}
.service-name{margin-top:22px;font-size:26px;font-weight:500;color:#333;text-transform:uppercase}
.service-text{margin-top:8px;font-size:21px;line-height:1.45;color:var(--muted)}

.cta{position:absolute;left:0;top:1952px;width:1200px;height:448px;background:var(--red);text-align:center;color:var(--white)}
.cta-title{margin-top:52px;font-size:54px;font-weight:700;text-transform:uppercase}
.cta-text{margin:34px auto 0;width:980px;font-size:27px;line-height:1.55}
.btn-light{display:inline-block;margin-top:36px;background:var(--white);color:var(--navy);font-size:30px;font-weight:600;padding:20px 52px;text-transform:uppercase}

.site-footer{position:absolute;left:0;top:2400px;width:1200px;height:268px;background:var(--navy-deep);display:flex;align-items:center;justify-content:space-between;padding:0 80px;color:var(--white)}
.site-footer .brand{color:var(--white)}
.social{display:flex;gap:28px}
.social span{width:22px;height:22px;border-radius:50%;background:var(--white);display:block}
.copyright{font-size:20px;color:#c9ccd6}
</style>
</head>
<body>

<header class="site-header">
  <div class="brand"><span class="brand-dot"></span><span>Steadfast Claim<br>Helpers USA</span></div>
  <nav class="main-nav">
    <span class="active">Home</span><span>About</span><span>Our Services</span><span>Contact</span>
  </nav>
</header>

<section class="hero">
  <div class="hero-photo" role="img" aria-label="Photo of a smiling older couple embracing outdoors"></div>
  <div class="hero-fade"></div>
  <div class="hero-copy">
    <h1 class="hero-title">Social Security<br>Disability Benefits</h1>
    <p class="hero-sub">You may be eligible for as much<br>as $1,700 per months!</p>
    <a class="btn-primary">Get My Free Evaluation</a>
  </div>
</section>

<section class="qualify">
  <h2 class="qualify-title">You may get paid for your disability<span>Keeping you out of work!</span></h2>
  <div class="rule"></div>
  <p class="intro">Lorem Ipsum is simply dummy the printing and typesetting industry. Lorem Ipsum is simply dummy the printing and typesetting industry.</p>
  <h3 class="checklist-title">Do I quality?</h3>
  <ul class="checklist">
    <li><svg viewBox="0 0 26 26"><rect x="2" y="2" width="22" height="22" fill="none" stroke="#e8232b" stroke-width="3"/><path d="M7 13l4 4 9-10" fill="none" stroke="#e8232b" stroke-width="3"/></svg>Bullet points content here</li>
    <li><svg viewBox="0 0 26 26"><rect x="2" y="2" width="22" height="22" fill="none" stroke="#e8232b" stroke-width="3"/><path d="M7 13l4 4 9-10" fill="none" stroke="#e8232b" stroke-width="3"/></svg>Bullet points content here</li>
    <li><svg viewBox="0 0 26 26"><rect x="2" y="2" width="22" height="22" fill="none" stroke="#e8232b" stroke-width="3"/><path d="M7 13l4 4 9-10" fill="none" stroke="#e8232b" stroke-width="3"/></svg>Bullet points content here</li>
    <li><svg viewBox="0 0 26 26"><rect x="2" y="2" width="22" height="22" fill="none" stroke="#e8232b" stroke-width="3"/><path d="M7 13l4 4 9-10" fill="none" stroke="#e8232b" stroke-width="3"/></svg>Bullet points content here</li>
    <li><svg viewBox="0 0 26 26"><rect x="2" y="2" width="22" height="22" fill="none" stroke="#e8232b" stroke-width="3"/><path d="M7 13l4 4 9-10" fill="none" stroke="#e8232b" stroke-width="3"/></svg>Bullet points content here</li>
  </ul>
</section>

<section class="services">
  <div class="service">
    <div class="service-icon"><svg viewBox="0 0 70 70" fill="none" stroke="#fff" stroke-width="3.5"><circle cx="35" cy="30" r="18"/><path d="M35 19v22M41 24c-2-2-10-3-11 1s11 4 11 9-9 4-12 1"/><path d="M8 56h54"/></svg></div>
    <h4 class="service-name">Service Name Here</h4>
    <p class="service-text">Lorem Ipsum is simply<br>dummy text of the printing</p>
  </div>
  <div class="service">
    <div class="service-icon is-green"><svg viewBox="0 0 70 70" fill="none" stroke="#fff" stroke-width="3.5"><rect x="16" y="12" width="38" height="48" rx="3"/><path d="M26 12v-4h18v4M24 28l4 4 8-8M24 46h22M40 30h6"/></svg></div>
    <h4 class="service-name">Service Name Here</h4>
    <p class="service-text">Lorem Ipsum is simply<br>dummy text of the printing</p>
  </div>
  <div class="service">
    <div class="service-icon"><svg viewBox="0 0 70 70" fill="none" stroke="#fff" stroke-width="3.5"><rect x="16" y="30" width="38" height="30" rx="3"/><path d="M24 30v-8a11 11 0 0 1 22 0v8M35 40v10"/></svg></div>
    <h4 class="service-name">Service Name Here</h4>
    <p class="service-text">Lorem Ipsum is simply<br>dummy text of the printing</p>
  </div>
</section>

<section class="cta">
  <h2 class="cta-title">Take Action Now</h2>
  <p class="cta-text">Lorem Ipsum is simply dummy text of the printing and typesetting industry. Lorem Ipsum has been industry's standard dummy text ever since the 1500s, when an unknown printer</p>
  <a class="btn-light">Claim Now Online</a>
</section>

<footer class="site-footer">
  <div class="brand"><span class="brand-dot"></span><span>Steadfast Claim<br>Helpers USA</span></div>
  <div class="social" aria-label="Social links"><span></span><span></span><span></span><span></span></div>
  <p class="copyright">Copyright © 2019 All Rights</p>
</footer>

</body>
</html>
```